Website for "Bright Meadow Ltd" cleaning bsuiness

We require a website to expose our business to the local market. We want to provide background on who we are and what we do but in an easily digestible way. We clean domestic and commercial premises and want to provide a list of all of our services to potential customers. We operate out of Warrington in the UK.

We would like the website to be animated in some way so that the experience of using it is not dull or mundane. This website needs to be an extension of our company.

Target Market(s)

30 - 60 year olds for Domestic plus commercial clients

Industry/Entity Type

Cleaning Service

Coding

Coded - Design and coding required

Number of Pages Required

4 page

Font styles to use
Sans Serif

Colors
0455a3
3176b5
85acd3
cfdeed
ffffff
000000
1b1b1b
c8c8c8
757575

Requirements
Must have
• Logo which has been provided. Theme based around the logo and its colours. Simple layout to avoid confusion.
Nice to have
• Animations where possible to impress the customer.
Should not have
• any pictures of cleaning equipment, fairies, maids etc

```html
<!DOCTYPE html>
<html lang="en">
<head>
<meta charset="utf-8">
<title>Bright Meadow Ltd – Cleaning Services in Warrington</title>
<link rel="stylesheet" href="https://fonts.googleapis.com/css2?family=Open+Sans:wght@400;600&family=Raleway:wght@400;500&display=swap">
<style>
:root{
  --blue:#0455a3;
  --blue-mid:#3176b5;
  --blue-bright:#1e7fe6;
  --navy:#0a2096;
  --blue-soft:#85acd3;
  --blue-pale:#cfdeed;
  --white:#ffffff;
  --black:#000000;
  --ink:#1b1b1b;
  --grey:#c8c8c8;
  --grey-dark:#757575;
  --footer:#0c0c0c;
}
*{margin:0;padding:0;box-sizing:border-box}
html,body{width:782px;height:1200px;overflow:hidden;background:var(--white)}
body{position:relative;font-family:"Open Sans",sans-serif;color:var(--ink)}
.abs{position:absolute}

/* hero */
.hero-photo{left:0;top:0;width:782px;height:445px;background:linear-gradient(160deg,#e9eef3 0%,#d6dde4 45%,#b9c0c7 75%,#8f9499 100%)}
.hero-floor{left:0;top:340px;width:782px;height:105px;background:linear-gradient(180deg,rgba(170,175,180,.4),rgba(150,150,152,.6))}
.slider-arrow{width:26px;height:26px;border-radius:50%;background:rgba(255,255,255,.8);display:flex;align-items:center;justify-content:center}
.slider-arrow.prev{left:36px;top:228px}
.slider-arrow.next{left:718px;top:228px}
.hero-title{left:90px;top:283px;width:322px;height:33px;background:var(--navy);clip-path:polygon(0 0,100% 0,88% 100%,0 100%);color:var(--white);font-family:"Raleway",sans-serif;font-weight:400;font-size:19px;padding:6px 0 0 33px;letter-spacing:.2px}
.hero-sub{left:90px;top:317px;width:328px;height:50px;background:rgba(255,255,255,.85);font-family:"Raleway",sans-serif;font-weight:400;font-size:17px;line-height:18px;color:var(--black);padding:8px 0 0 33px}
.hero-cta{left:90px;top:384px;width:147px;height:24px;background:var(--blue-bright);color:var(--white);font-family:"Raleway",sans-serif;font-size:13px;text-align:center;line-height:24px}

/* header */
.site-header{left:62px;top:0;width:654px;height:83px;background:var(--white);box-shadow:0 2px 6px rgba(0,0,0,.12)}
.brand{left:14px;top:24px;display:flex;align-items:center;gap:6px;font-family:"Open Sans",sans-serif;font-weight:600;font-size:15px;color:var(--navy)}
.brand-dot{width:14px;height:14px;border-radius:50%;background:var(--navy)}
.contact-line{font-size:6.5px;color:var(--blue-bright)}
.contact-line b{display:block;font-weight:400;font-size:8px;color:var(--grey-dark);margin-top:3px;white-space:nowrap}
.mail{left:301px;top:13px}
.call{left:427px;top:13px}
.head-icon{top:15px}
.header-cta{left:555px;top:12px;width:85px;height:24px;background:var(--blue-bright);color:var(--white);font-size:10px;font-weight:600;text-align:center;line-height:24px}
.main-nav{left:313px;top:56px;display:flex;gap:23px;font-size:8px;color:var(--ink);font-family:"Open Sans",sans-serif}
.main-nav .active{color:var(--navy);position:relative}
.main-nav .active::after{content:"";position:absolute;left:-8px;right:-8px;top:20px;height:2px;background:var(--navy)}

/* sections */
.section-title{width:782px;text-align:center;font-family:"Raleway",sans-serif;font-weight:400;font-size:21px;color:var(--black)}
.intro{left:94px;top:489px;width:594px;text-align:center;font-size:7.4px;line-height:11.2px;color:#444}
.feature{width:120px;text-align:center}
.feature-ring{width:62px;height:62px;margin:0 auto;border-radius:50%;border:1px solid var(--navy);display:flex;align-items:center;justify-content:center}
.feature-ring.filled{background:var(--blue-bright);border:none;box-shadow:0 0 0 5px #eceff2}
.feature-label{margin-top:20px;font-size:10px;font-weight:600;color:#333}
.divider{left:63px;top:704px;width:654px;border-top:1px dotted var(--grey)}
.service-photo{left:63px;top:775px;width:309px;height:186px;background:linear-gradient(180deg,#b9c7da 0%,#a8b9d1 60%,#f2f2f2 75%,#e6e6e6 100%)}
.service-head{left:392px;top:772px;font-size:9px;color:var(--ink)}
.service-lead{left:393px;top:789px;width:325px;font-size:6.8px;line-height:11px;color:#333}
.service-list{width:146px;list-style:none}
.service-list li{height:19px;display:flex;align-items:center;gap:10px;font-size:7px;color:#333;border-bottom:1px solid #eee}
.service-list li.plain{border:none;padding-left:20px}
.tick-circle{width:10px;height:10px;border-radius:50%;border:1px solid var(--blue-bright);display:flex;align-items:center;justify-content:center}

/* footer */
.site-footer{left:0;top:1002px;width:782px;height:160px;background:var(--footer);border-top:2px solid #555}
.foot-head{font-size:8px;color:var(--blue-bright)}
.foot-text{font-size:6.4px;line-height:9.6px;color:var(--grey-dark)}
.foot-links{list-style:none;font-size:6.4px;color:var(--grey-dark)}
.foot-links li{height:12.8px;display:flex;align-items:center;gap:8px}
.foot-links li::before{content:"";width:3px;height:3px;border-radius:50%;background:var(--grey-dark)}
.foot-links li.active{color:var(--blue-bright)}
.foot-links li.active::before{background:var(--blue-bright)}
.foot-field{width:128px;height:17px;background:var(--white);border:1px solid var(--grey);font-size:6.4px;color:var(--grey-dark);padding:4px 5px}
.foot-btn{left:663px;top:1129px;width:49px;height:13px;background:var(--blue-bright);color:var(--white);font-size:6.6px;font-weight:600;text-align:center;line-height:13px}
.bottom-bar{left:0;top:1162px;width:782px;height:38px;background:#070707}
.copyright{left:62px;top:1176px;font-size:6.4px;color:var(--white)}
.social{top:1175px;width:9px;height:9px;border-radius:50%;background:var(--white)}
</style>
</head>
<body>

<div class="abs hero-photo" role="img" aria-label="Bright, tidy office interior with desk, chair and water cooler"></div>
<div class="abs hero-floor"></div>
<div class="abs slider-arrow prev"><svg width="6" height="6"><path d="M5 0L1 3L5 6Z" fill="#999"/></svg></div>
<div class="abs slider-arrow next"><svg width="6" height="6"><path d="M1 0L5 3L1 6Z" fill="#999"/></svg></div>
<div class="abs hero-title">BRIGHT MEADOW</div>
<div class="abs hero-sub">Cleaning services company in<br>Warrington, UK</div>
<div class="abs hero-cta">Get a quote now</div>

<header class="abs site-header">
  <div class="abs brand"><span class="brand-dot"></span>Bright Meadow Ltd</div>
  <div class="abs contact-line mail">Mail Us<b>hi@bmclean.example</b></div>
  <svg class="abs head-icon" style="left:392px" width="16" height="16" viewBox="0 0 16 16"><circle cx="8" cy="8" r="7" fill="none" stroke="#1e7fe6" stroke-width="1.2"/><rect x="4.5" y="5.5" width="7" height="5" fill="none" stroke="#1e7fe6"/><path d="M4.5 5.5L8 8.5L11.5 5.5" fill="none" stroke="#1e7fe6"/></svg>
  <div class="abs" style="left:416px;top:12px;width:1px;height:24px;background:#ddd"></div>
  <div class="abs contact-line call">Call Us<b>216.555.0142</b></div>
  <svg class="abs head-icon" style="left:502px" width="16" height="16" viewBox="0 0 16 16"><circle cx="8" cy="8" r="7" fill="none" stroke="#1e7fe6" stroke-width="1.2"/><path d="M5.5 4.5l1.5 0 .7 2-1 .8a5 5 0 0 0 2 2l.8-1 2 .7v1.5a1 1 0 0 1-1 1A6 6 0 0 1 4.5 5.5a1 1 0 0 1 1-1z" fill="#1e7fe6"/></svg>
  <div class="abs header-cta">CONTACT US</div>
  <nav class="abs main-nav">
    <span class="active">HOME</span><span>ABOUT US</span><span>PRODUCTS</span><span>TESTIMONIALS</span><span>CONTACT US</span>
  </nav>
</header>

<h2 class="abs section-title" style="top:458px">Who we are</h2>
<p class="abs intro">Lorem ipsum dolor sit amet, consectetur adipiscing elit. Duis in neque sapien. Pellentesque fringilla mauris vel sodales faucibus. Quisque euismod quam eu libero cursus, vel sollicitudin lectus varius. Vivamus tincidunt pellentesque sollicitudin. Nunc in massa efficitur, sodales magna non, varius justo. Nullam feugiat mollis magna, et lacinia turpis fermentum a. Donec non sapien eget est rhoncus efficitur vel hendrerit turpis. Integer neque leo, placerat nec dui venenatis, lacinia tincidunt eros. Proin luctus ultrices arcu, ac pulvinar diam faucibus at. Aenean lobortis, nibh sed pulvinar convallis, urna tortor tincidunt lorem, nec mattis libero dolor quis justo. Aenean a libero eu nulla tempor vehicula.</p>

<div class="abs feature" style="left:100px;top:568px">
  <div class="feature-ring"><svg width="22" height="24" viewBox="0 0 22 24"><path d="M11 3C11 3 4 11 4 16a7 7 0 0 0 14 0C18 11 11 3 11 3z" fill="#0a2096"/></svg></div>
  <div class="feature-label">Superior Cleaning</div>
</div>
<div class="abs feature" style="left:235px;top:568px">
  <div class="feature-ring filled"><svg width="24" height="24" viewBox="0 0 24 24"><path d="M5 21C5 11 11 4 21 3C21 13 14 20 5 21z" fill="#fff"/><path d="M5 21L14 11" stroke="#1e7fe6" stroke-width="1.4"/></svg></div>
  <div class="feature-label">100% Natural</div>
</div>
<div class="abs feature" style="left:382px;top:568px">
  <div class="feature-ring"><svg width="24" height="20" viewBox="0 0 24 20"><path d="M2 10l7 7L22 2" fill="none" stroke="#0a2096" stroke-width="4"/></svg></div>
  <div class="feature-label">Affordable Rates</div>
</div>
<div class="abs feature" style="left:536px;top:568px">
  <div class="feature-ring"><svg width="36" height="24" viewBox="0 0 36 24"><circle cx="23" cy="5" r="3" fill="#0a2096"/><path d="M3 9l14 10L33 7" fill="none" stroke="#0a2096" stroke-width="3"/><path d="M8 9l9 6 8-6" fill="none" stroke="#0a2096" stroke-width="2"/></svg></div>
  <div class="feature-label">Satisfaction Guranteed</div>
</div>

<div class="abs divider"></div>

<h2 class="abs section-title" style="top:720px">What we do</h2>
<div class="abs service-photo" role="img" aria-label="Clean white desk with potted orchid and pinboard against a pale blue wall"></div>
<div class="abs service-head">Lorem ipsum</div>
<p class="abs service-lead">Lorem ipsum dolor sit amet, consectetur adipiscing elit. Duis in neque sapien. Pellentesque fringilla mauris vel sodales faucibus.</p>

<ul class="abs service-list" style="left:392px;top:827px;width:146px">
  <li><span class="tick-circle"><svg width="4" height="5"><path d="M1 0L3.5 2.5L1 5" fill="none" stroke="#1e7fe6"/></svg></span>Residential Cleaning</li>
  <li><span class="tick-circle"><svg width="4" height="5"><path d="M1 0L3.5 2.5L1 5" fill="none" stroke="#1e7fe6"/></svg></span>Commercial Cleaning</li>
  <li><span class="tick-circle"><svg width="4" height="5"><path d="M1 0L3.5 2.5L1 5" fill="none" stroke="#1e7fe6"/></svg></span>Green Cleaning</li>
  <li><span class="tick-circle"><svg width="4" height="5"><path d="M1 0L3.5 2.5L1 5" fill="none" stroke="#1e7fe6"/></svg></span>Move-in/out Cleaning</li>
  <li><span class="tick-circle"><svg width="4" height="5"><path d="M1 0L3.5 2.5L1 5" fill="none" stroke="#1e7fe6"/></svg></span>Vacant Home Cleaning</li>
  <li><span class="tick-circle"><svg width="4" height="5"><path d="M1 0L3.5 2.5L1 5" fill="none" stroke="#1e7fe6"/></svg></span>Window Cleaning</li>
  <li style="border:none"><span class="tick-circle"><svg width="4" height="5"><path d="M1 0L3.5 2.5L1 5" fill="none" stroke="#1e7fe6"/></svg></span>Professional Organization</li>
</ul>
<ul class="abs service-list" style="left:571px;top:828px">
  <li><span class="tick-circle"><svg width="4" height="5"><path d="M1 0L3.5 2.5L1 5" fill="none" stroke="#1e7fe6"/></svg></span>Construction Clean-up</li>
  <li class="plain">And Much More..</li>
</ul>

<footer class="abs site-footer"></footer>
<div class="abs foot-head" style="left:62px;top:1028px">ABOUT US</div>
<p class="abs foot-text" style="left:62px;top:1045px;width:140px">Lorem ipsum dolor sit amet, consectetur adipiscing elit. Nullam venenatis velit blandit est condimentum aliquet. Curabitur ut libero justo. Nulla ut ex facilisis, tincidunt quam vitae, iaculis orci. Nullam eu faucibus nibh.</p>
<div class="abs foot-text" style="left:166px;top:1115px;display:flex;gap:4px;align-items:center">More <svg width="9" height="9"><circle cx="4.5" cy="4.5" r="4" fill="none" stroke="#757575"/><path d="M2.5 4.5h4M5 3l1.5 1.5L5 6" fill="none" stroke="#757575"/></svg></div>

<div class="abs foot-head" style="left:264px;top:1028px">USEFUL LINKS</div>
<ul class="abs foot-links" style="left:264px;top:1044px">
  <li class="active">Home</li><li>About Us</li><li>Our Services</li><li>Steam Cleaning</li><li>Gallery</li><li>Testimonials</li><li>Contact</li>
</ul>

<div class="abs foot-head" style="left:394px;top:1028px">GET IN TOUCH</div>
<p class="abs foot-text" style="left:396px;top:1045px;width:138px">Doloreiur quia commolu ptatemp dolupta orepererum tibusam eumenis et consent accullignis dentibese</p>
<div class="abs foot-text" style="left:396px;top:1082px;line-height:12.8px">
  <div><svg width="6" height="7"><path d="M3 7L0.5 3A2.5 2.5 0 1 1 5.5 3Z" fill="#aaa"/></svg>&nbsp;&nbsp;12 Linden Row, Warrington WA9 4ZX</div>
  <div><svg width="6" height="6"><path d="M1 0h1.5l.5 1.5-1 .8a3 3 0 0 0 1.7 1.7l.8-1L6 3.5V5a1 1 0 0 1-1 1A5 5 0 0 1 0 1a1 1 0 0 1 1-1z" fill="#aaa"/></svg>&nbsp;&nbsp;216.555.0142</div>
  <div><svg width="7" height="5"><rect width="7" height="5" fill="#aaa"/><path d="M0 0l3.5 2.5L7 0" fill="none" stroke="#0c0c0c" stroke-width=".8"/></svg>&nbsp;&nbsp;office@bmclean.example</div>
</div>

<div class="abs foot-head" style="left:582px;top:1028px">CONTACT</div>
<p class="abs foot-text" style="left:584px;top:1045px;width:135px">Doloreiur quia commolu ptatemp dolupta orepererum</p>
<div class="abs foot-field" style="left:585px;top:1076px">Email</div>
<div class="abs foot-field" style="left:585px;top:1100px;display:flex;justify-content:space-between">Contact For <svg width="7" height="5"><path d="M0.5 1l3 3 3-3" fill="none" stroke="#999"/></svg></div>
<div class="abs foot-btn">CONTACT</div>

<div class="abs bottom-bar"></div>
<div class="abs copyright">© 2016 bmclean.example. All rights reserved.</div>
<span class="abs social" style="left:650px"></span>
<span class="abs social" style="left:668px"></span>
<span class="abs social" style="left:686px"></span>
<span class="abs social" style="left:705px"></span>

</body>
</html>
```